The Brightwell Clinic :

At The Brightwell Clinic our goal is to provide the most skilled and advanced examination and treatment of the upper neck for superior long-term outcomes for those experiencing headache or migraine.

If a spinal disorder is responsible for the headache and migraine condition the disorder will involve one or more of the top three spinal segments. The fundamental and most powerful feature of The Brightwell Clinic is our method of examining the movements of the top three spinal segments.

We would like the design should communicate professionalism and specialisation.
Updates

Don't necessarily have to have the photos provided.Photo was used for promotional material. I dont have a logo as yet what I  would also like designed.

Project Deadline Extended
Reason: Opening has been delayed due to construction issues of building.

Industry/Entity Type

Clinic

Contact Information for Business Card

The Brightwell Clinic
Suite 3, Oakvale Heath Centre
87 Ferncliff Drive, Port Macquarie NSW 2444
Tel : 63 71 2946 www.thebrightwellclinic.com.au

Requirements
Must have
• Mr Carl Pettigrew
Senior Physiotherapist / Senior Accredited Exercise Physiologist
Ba. App. Sc. (Physiotherapy), Ba Sp. Sc. (Exercise Science), Dip. R.M, MAPA, MESSA, MSMA, MACSM.

Appointment area on back of card

```html
<!DOCTYPE html>
<html lang="en">
<head>
<meta charset="utf-8">
<title>Brightwell Clinic – Appointment Card (Back)</title>
<link rel="stylesheet" href="https://fonts.googleapis.com/css2?family=Questrial&display=swap">
<style>
  :root {
    --paper: #ffffff;
    --rule: #6f6f6f;
    --brand-purple: #6a2c85;
    --mark-grey: #b9b4bd;
    --photo-light: #f6f1ec;
    --photo-mid: #efe2d6;
    --photo-warm: #e8d3c2;
  }
  html, body {
    margin: 0;
    padding: 0;
    overflow: hidden;
    background: var(--paper);
  }
  .card {
    position: relative;
    width: 1200px;
    height: 694px;
    overflow: hidden;
    background: var(--paper);
    font-family: "Questrial", "Century Gothic", sans-serif;
  }
  .portrait-area {
    position: absolute;
    top: 0;
    right: 0;
    width: 600px;
    height: 694px;
    background:
      linear-gradient(90deg, var(--paper) 0%, rgba(255,255,255,0) 28%),
      radial-gradient(ellipse at 72% 45%, var(--photo-warm) 0%, var(--photo-mid) 45%, var(--photo-light) 80%);
  }
  .appointment-lines {
    position: absolute;
    left: 0;
    top: 0;
  }
  .appointment-lines line {
    stroke: var(--rule);
    stroke-width: 1;
  }
  .clinic-name {
    position: absolute;
    left: 760px;
    top: 600px;
    display: flex;
    align-items: center;
    gap: 14px;
  }
  .clinic-name-dot {
    width: 26px;
    height: 26px;
    border-radius: 50%;
    background: var(--mark-grey);
  }
  .clinic-name-text {
    font-size: 32px;
    line-height: 1;
    color: var(--brand-purple);
  }
</style>
</head>
<body>
  <div class="card">
    <div class="portrait-area" role="img" aria-label="Soft promotional portrait of a smiling patient"></div>

    <svg class="appointment-lines" width="1200" height="694" aria-label="Appointment writing lines">
      <line x1="68" y1="161.5" x2="606" y2="161.5"/>
      <line x1="68" y1="200.5" x2="606" y2="200.5"/>
      <line x1="68" y1="238.5" x2="606" y2="238.5"/>
      <line x1="68" y1="276.5" x2="606" y2="276.5"/>
      <line x1="68" y1="315.5" x2="606" y2="315.5"/>
      <line x1="68" y1="353.5" x2="606" y2="353.5"/>
      <line x1="68" y1="391.5" x2="606" y2="391.5"/>
      <line x1="324" y1="477.5" x2="606" y2="477.5"/>
    </svg>

    <div class="clinic-name">
      <div class="clinic-name-dot"></div>
      <span class="clinic-name-text">Brightwell Clinic</span>
    </div>
  </div>
</body>
</html>
```